Business card for job seeker professional

Hi. I'm a sale and marketing professional who's just moved to Australia and looking for a job. I would like to have a business card designed for me, which I can use for job interviews/networking. Given Pronexa increasing importance in the job market, I would like my public profile link (http://au.pronexa.com/in/dorianmalvek/) to be incorporated into my details.

```html
<!DOCTYPE html>
<html lang="en">
<head>
<meta charset="utf-8">
<title>Dorian Malvek – Business Card</title>
<link rel="stylesheet" href="https://fonts.googleapis.com/css2?family=Mulish:wght@700;800&family=Libre+Baskerville:wght@700&display=swap">
<style>
  :root {
    --backdrop: #e6e7e9;
    --card: #ffffff;
    --brand-blue: #1a68a0;
    --ink: #111111;
    --icon-blue: #2a86c4;
  }
  html, body {
    margin: 0;
    padding: 0;
    width: 1200px;
    height: 1000px;
    overflow: hidden;
    background: var(--backdrop);
  }
  .card {
    position: absolute;
    left: 250px;
    top: 298px;
    width: 698px;
    height: 403px;
    background: var(--card);
    border-radius: 30px;
    overflow: hidden;
    box-shadow: 5px 6px 5px rgba(0, 0, 0, 0.45);
  }
  .card__band {
    position: absolute;
    left: 0;
    top: 0;
    width: 100%;
    height: 138px;
    background: var(--brand-blue);
  }
  .name {
    position: absolute;
    left: 50px;
    margin: 0;
    font-family: "Mulish", "Century Gothic", sans-serif;
    font-weight: 800;
    line-height: 1;
    letter-spacing: -0.5px;
  }
  .name--first {
    top: 78px;
    font-size: 60px;
    color: var(--card);
  }
  .name--last {
    top: 139px;
    font-size: 43px;
    color: var(--brand-blue);
  }
  .contacts {
    position: absolute;
    left: 52px;
    top: 276px;
    margin: 0;
    padding: 0;
    list-style: none;
    font-family: "Libre Baskerville", "Baskerville", serif;
    font-weight: 700;
    font-size: 17px;
  }
  .contacts__item {
    display: flex;
    align-items: center;
    height: 31px;
    white-space: nowrap;
  }
  .contacts__label { color: var(--brand-blue); }
  .contacts__value { color: var(--ink); }
  .contacts__link { color: var(--brand-blue); }
  .contacts__icon {
    width: 22px;
    height: 22px;
    margin: 0 3px 0 2px;
  }
  .network-name {
    display: flex;
    align-items: center;
    color: var(--ink);
    margin-right: 8px;
  }
  .network-name__mark {
    width: 14px;
    height: 14px;
    margin-left: 4px;
    background: var(--brand-blue);
  }
</style>
</head>
<body>
  <article class="card">
    <div class="card__band"></div>
    <h1 class="name name--first">Dorian</h1>
    <p class="name name--last">Malvek</p>

    <ul class="contacts">
      <li class="contacts__item">
        <span class="contacts__label">Email</span>
        <svg class="contacts__icon" viewBox="0 0 22 22" aria-hidden="true">
          <path d="M2 9 L11 2 L20 9 V20 H2 Z" fill="var(--icon-blue)"/>
          <path d="M4 9 L11 4 L18 9 L11 14 Z" fill="#fff"/>
          <path d="M2 9 L11 15 L20 9" fill="none" stroke="#fff" stroke-width="1.3"/>
          <path d="M2 20 L9 13 M20 20 L13 13" stroke="#fff" stroke-width="1.2"/>
        </svg>
        <span class="contacts__value">example-mail@examplesite.com</span>
      </li>
      <li class="contacts__item">
        <span class="contacts__label">Mobile</span>
        <svg class="contacts__icon" viewBox="0 0 22 22" aria-hidden="true">
          <path d="M5 2 C3 3 2 5 3 8 C5 13 9 17 14 19 C17 20 19 19 20 17 L16 13 L13 15 C11 14 8 11 7 9 L9 6 Z" fill="var(--icon-blue)"/>
        </svg>
        <span class="contacts__value">0000 000 000</span>
      </li>
      <li class="contacts__item">
        <span class="network-name">Pronexa<span class="network-name__mark"></span></span>
        <span class="contacts__link">http://au.pronexa.com/in/dorianmalvek/</span>
      </li>
    </ul>
  </article>
</body>
</html>
```